Business card design for Sable Crestway

We need business cards designed for our new marketing consulting company, Sable Crestway. Our services include marketing strategy, go-to-market and launch planning, growth strategy, and execution. We serve medical technology and health technology companies, from startups to well-established growth companies.

The business cards should feel professional, credible, reliable and trustworthy, and should instill confidence. Also bold, creative, and modern.

The design must use the Sable Crestway logo.

The primary brand color is this orange: #FF5501
A secondary color that you can use is this gray: #282B2D
I would prefer only to use the orange and gray. But if you feel you really need an additional accent color (please use it very sparingly, as little as possible), you can use this blue for small accent purposes: #009FED

Attached are the logo files. The main logo is the one with a little bit of orange on the left and the rest is gray.

The business card should include the following:

Sable Crestway logo
First name and last name
Title
Email address
Phone number and type (in whatever order looks best for the design
Website (the website does not need to be in the same block as the personal info)

For example:

Wren Tasker
Founder & Principal
wren@sablecrestway.com
+1.415.836.2094 mobile (can use "." or spaces in between blocks of numbers)
sablecrestway.com (somewhere on the card, it does not need to be with the personal info; and note that there is no "www." at the beginning)

Note that there will be no address listed on the business card.

Target Market(s)

Executives (CEO, head of marketing, head of sales) at medical technology and health technology companies, mostly in their 40s and older, well-educated, often with advanced degrees. They are strategic thinkers, responsible for budgets, and familiar with P&L. Their comfort with and trust in using outside consultants varies.

Industry/Entity Type

Medical technology and health technology companies.

Contact Information for Business Card

See project description

Font styles to use
Sans Serif

Requirements
Must have
• Logo and see Business card details section above.

```html
<!DOCTYPE html>
<html lang="en">
<head>
<meta charset="utf-8">
<title>Sable Crestway — Business Card</title>
<link rel="stylesheet" href="https://fonts.googleapis.com/css2?family=Montserrat:wght@400;500;600;700;800&display=swap">
<style>
  :root {
    --orange: #ff5501;
    --card-gray: #2a2d2f;
    --stage: #d9d9d7;
    --white: #ffffff;
    --muted: #e8e8e8;
  }
  * { box-sizing: border-box; margin: 0; padding: 0; }
  html, body { width: 1200px; height: 900px; overflow: hidden; }
  body {
    background: var(--stage);
    font-family: "Montserrat", sans-serif;
    position: relative;
  }
  .card {
    position: absolute;
    top: 152px;
    width: 340px;
    height: 595px;
    background: var(--card-gray);
    box-shadow: 0 14px 30px rgba(0,0,0,0.25);
    overflow: hidden;
  }
  .card--front { left: 220px; }
  .card--back { left: 640px; }

  .brand {
    position: absolute;
    display: flex;
    align-items: center;
    gap: 16px;
  }
  .brand__dot {
    width: 22px; height: 22px;
    border-radius: 50%;
    background: var(--orange);
    flex: none;
  }
  .brand__name {
    color: var(--white);
    font-weight: 600;
    font-size: 23px;
    line-height: 1.1;
    letter-spacing: 0.2em;
    text-transform: uppercase;
  }
  .card--front .brand { left: 34px; top: 148px; }
  .card--back .brand { left: 50%; top: 50%; transform: translate(-50%, -50%); }

  .person {
    position: absolute;
    left: 0; top: 392px;
    padding-left: 40px;
  }
  .person__bar {
    position: absolute;
    left: 0; top: 4px;
    width: 22px; height: 52px;
    background: var(--orange);
  }
  .person__name {
    color: var(--orange);
    font-weight: 800;
    font-size: 27px;
    letter-spacing: 0.01em;
    text-transform: uppercase;
    line-height: 1.05;
  }
  .person__title {
    color: var(--white);
    font-weight: 500;
    font-size: 15px;
    margin-top: 4px;
  }

  .contacts {
    position: absolute;
    left: 44px; top: 476px;
    list-style: none;
  }
  .contacts li {
    display: flex;
    align-items: center;
    gap: 10px;
    color: var(--muted);
    font-size: 14px;
    font-weight: 500;
    margin-bottom: 9px;
  }
  .contacts svg { width: 14px; height: 14px; flex: none; fill: var(--orange); }

  .card__band {
    position: absolute;
    left: 0; right: 0; bottom: 0;
    height: 16px;
    background: var(--orange);
  }
</style>
</head>
<body>

<section class="card card--front" aria-label="Business card front">
  <div class="brand">
    <span class="brand__dot"></span>
    <span class="brand__name">Sable<br>Crestway</span>
  </div>

  <div class="person">
    <span class="person__bar"></span>
    <h1 class="person__name">Wren Tasker</h1>
    <p class="person__title">Founder &amp; Principal</p>
  </div>

  <ul class="contacts">
    <li>
      <svg viewBox="0 0 24 24" aria-hidden="true"><path d="M6.6 10.8a15.5 15.5 0 0 0 6.6 6.6l2.2-2.2a1 1 0 0 1 1-.25 11.4 11.4 0 0 0 3.6.57 1 1 0 0 1 1 1V20a1 1 0 0 1-1 1A17 17 0 0 1 3 4a1 1 0 0 1 1-1h3.5a1 1 0 0 1 1 1c0 1.25.2 2.45.57 3.57a1 1 0 0 1-.25 1z"/></svg>
      +1.415.836.2094
    </li>
    <li>
      <svg viewBox="0 0 24 24" aria-hidden="true"><path d="M2 5h20v14H2z M2 5l10 8 10-8" fill="none" stroke="#ff5501" stroke-width="0"/><path d="M2 6.5 12 13l10-6.5V19H2z"/><path d="M2 5h20l-10 6.5z"/></svg>
      wren@sablecrestway.com
    </li>
    <li>
      <svg viewBox="0 0 24 24" aria-hidden="true"><path d="M12 2a10 10 0 1 0 0 20 10 10 0 0 0 0-20zm6.9 6h-3a15 15 0 0 0-1.3-3.9A8 8 0 0 1 18.9 8zM12 4c.8 1.2 1.5 2.5 1.9 4h-3.8c.4-1.5 1.1-2.8 1.9-4zM4.3 14a8 8 0 0 1 0-4h3.4a16 16 0 0 0 0 4zm.8 2h3a15 15 0 0 0 1.3 3.9A8 8 0 0 1 5.1 16zm3-8h-3a8 8 0 0 1 4.3-3.9A15 15 0 0 0 8.1 8zM12 20c-.8-1.2-1.5-2.5-1.9-4h3.8c-.4 1.5-1.1 2.8-1.9 4zm2.3-6H9.7a14 14 0 0 1 0-4h4.6a14 14 0 0 1 0 4zm.3 5.9a15 15 0 0 0 1.3-3.9h3a8 8 0 0 1-4.3 3.9zm1.7-5.9a16 16 0 0 0 0-4h3.4a8 8 0 0 1 0 4z"/></svg>
      sablecrestway.com
    </li>
  </ul>

  <div class="card__band"></div>
</section>

<section class="card card--back" aria-label="Business card back">
  <div class="brand">
    <span class="brand__dot"></span>
    <span class="brand__name">Sable<br>Crestway</span>
  </div>
</section>

</body>
</html>
```